Brightwell Assist Public Benefit Corporation - Initial Website

We need to develop an initial website for Brightwell Assist PBC. We are a startup managed business services provider focused on small business owners, entrepreneurs and their employees. We are a public benefit corporation and our public mission is to help business owners, entrepreneurs and their employees overcome the challenges that hold them back from reaching personal and professional success.
Our primary service offerings are managed business services that allow us to support the day-to-day operations of the businesses we support. This ongoing support provides the necessary pre-requisite relationship so we can provide effective and timely support when their organizations are experiencing challenges and moments of crisis. In those moments, it is our opportunity to help them overcome those challenges and stay on track for business utopia.
Our services are provided on a contract basis for a fixed monthly fee. We want to build strong relationships that help our clients grow their businesses while taking away the stresses associated with the backend of the business operations.
Finally, our public benefit is that we provide crisis invention, critical incident support, and mental health services to business owners and their employees during challenging times in an effort to improve their overall quality of life.

Coding

Coded - Design and coding required

```html
<!DOCTYPE html>
<html lang="en">
<head>
<meta charset="UTF-8">
<title>Brightwell Assist PBC</title>
<link href="https://fonts.googleapis.com/css2?family=Montserrat:wght@500;600;700&family=Poppins:wght@400;500;600&display=swap" rel="stylesheet">
<style>
:root{
  --navy:#13205a;
  --navy-deep:#0f1a4d;
  --orange:#f77b0b;
  --ink:#151515;
  --muted:#666a73;
  --line:#e3e5ea;
  --soft:#f4f5f8;
  --white:#ffffff;
}
*{box-sizing:border-box;margin:0;padding:0}
html,body{width:1200px;height:5146px;overflow:hidden}
body{font-family:'Poppins',sans-serif;color:var(--ink);background:var(--white);position:relative}
section,header,footer{position:absolute;left:0;width:1200px}
.abs{position:absolute}
h1,h2,h3{font-family:'Montserrat',sans-serif}
.eyebrow{font-size:11px;font-weight:500;color:var(--orange);letter-spacing:.3px;text-transform:uppercase;display:flex;align-items:center;gap:8px}
.eyebrow::before{content:"";width:7px;height:7px;border-radius:50%;background:var(--orange)}
.arrow-dot{width:38px;height:38px;border-radius:50%;background:var(--orange);display:inline-flex;align-items:center;justify-content:center}
.ph{background:linear-gradient(135deg,#8a93a8,#c9ccd4)}

/* header */
.site-header{top:0;height:80px;background:var(--white);border-bottom:1px solid var(--line)}
.brand{display:flex;align-items:center;gap:8px;color:var(--navy);font-family:'Poppins',sans-serif;font-weight:600}
.brand-mark{width:12px;height:12px;border-radius:50%;background:var(--orange)}
.brand-text{line-height:1}
.brand-text .n{font-size:22px;display:block}
.brand-text .s{font-size:8.5px;letter-spacing:.4px;display:block;margin-top:3px;text-transform:uppercase}
.nav{left:452px;top:32px;display:flex;gap:46px;font-size:12px;color:var(--ink)}
.nav span::after{content:" ▾";font-size:9px}
.btn-contact{left:924px;top:23px;width:136px;height:36px;border-radius:18px;background:var(--orange);color:#fff;font-size:12px;display:flex;align-items:center;justify-content:center;gap:8px}

/* hero */
.hero{top:80px;height:808px;background:var(--navy-deep)}
.hero-photo{left:0;top:0;width:1200px;height:540px;background:linear-gradient(180deg,#6f7ea6 0%,#3c4c7e 60%,#0f1a4d 100%)}
.hero h1{left:672px;top:130px;width:420px;font-size:52px;line-height:62px;color:#fff;font-weight:700}
.hero-cta{left:672px;top:334px;display:flex;align-items:center;gap:14px;color:#fff;font-size:14px;font-weight:500}
.hero-rule{left:140px;top:492px;width:920px;height:3px;background:#fff}
.hero .eyebrow{left:140px;top:534px}
.hero-note{left:622px;top:530px;width:440px;font-size:12px;line-height:22px;color:#fff}
.hero-card{top:606px;width:290px;height:110px;background:#fff;display:flex}
.hero-card .t{width:146px;padding:20px 18px;font-size:12px;font-weight:500;line-height:18px;color:var(--ink);position:relative}
.hero-card .t svg{position:absolute;left:18px;bottom:16px}
.hero-card .img{flex:1}

/* goal */
.goal{top:888px;height:153px;border-bottom:1px solid var(--line);text-align:center}
.goal p{margin-top:88px;font-size:15px;color:#555a66}
.goal p b{color:var(--orange);font-weight:400}

/* services */
.services{top:1041px;height:673px;background:linear-gradient(180deg,#fff 0%,#f1f2f6 100%);overflow:hidden}
.services .eyebrow{left:140px;top:54px}
.services h2{left:140px;top:74px;width:400px;font-size:36px;line-height:48px;font-weight:600;white-space:nowrap}
.stat{top:70px;width:200px}
.stat .num{font-family:'Montserrat',sans-serif;font-size:50px;font-weight:500;color:var(--orange);line-height:1;display:inline-block}
.stat .unit{font-size:11px;vertical-align:top;margin-left:14px;color:var(--ink)}
.stat .rule{height:1px;background:#cfd2da;margin:16px 0 18px}
.stat p{font-size:11px;line-height:18px;color:#333}
.svc{top:258px;width:290px;text-align:center}
.svc .img{height:150px}
.svc h3{font-family:'Poppins',sans-serif;font-size:15px;font-weight:500;margin-top:32px}
.svc p{font-size:11.5px;line-height:18px;color:var(--muted);margin:10px auto 0;width:250px}
.view-all{left:512px;top:542px;display:flex;align-items:center;gap:14px;font-size:14px;font-weight:500}
.tower{left:936px;top:480px;width:264px;height:193px;background:linear-gradient(160deg,#d4d6db,#8d9099);clip-path:polygon(100% 0,100% 100%,0 100%,70% 18%)}

/* why */
.why{top:1714px;height:632px;text-align:center}
.why .eyebrow{left:0;width:1200px;justify-content:center;top:90px}
.why h2{left:0;width:1200px;top:114px;font-size:38px;line-height:48px;font-weight:600}
.why .lead{left:150px;width:900px;top:222px;font-size:12px;line-height:23px;color:#444}
.feature{width:276px;height:80px;border:1px solid var(--line);box-shadow:0 4px 10px rgba(0,0,0,.06);display:flex;align-items:center;gap:20px;padding-left:22px;font-size:13px;font-weight:500;background:#fff}
.ico{width:46px;height:46px;border-radius:50%;display:flex;align-items:center;justify-content:center;flex:none}
.ico.o{background:var(--orange)}
.ico.n{background:var(--navy)}

/* how */
.how{top:2346px;height:602px;background:var(--soft)}
.how-photo{left:140px;top:74px;width:400px;height:400px;background:linear-gradient(135deg,#e6e7ea,#b9bcc4)}
.how-accent{left:140px;top:240px;width:272px;height:234px;background:linear-gradient(135deg,#f79a3c,#e8740c)}
.how-laptop{left:360px;top:266px;width:272px;height:196px;background:linear-gradient(135deg,#d7d9de,#9fa3ad);clip-path:polygon(38% 0,100% 0,62% 100%,0 100%)}
.how .eyebrow{left:684px;top:108px}
.how h2{left:684px;top:130px;font-size:36px;line-height:48px;font-weight:500}
.step{left:684px;width:380px;display:flex;gap:22px}
.step .ico{background:#fff;box-shadow:0 3px 8px rgba(0,0,0,.1);width:48px;height:48px}
.step h3{font-family:'Poppins',sans-serif;font-size:15px;font-weight:500;margin-top:4px}
.step p{font-size:11.5px;line-height:22px;color:var(--muted);margin-top:4px}

/* testimonial */
.testimonial{top:2948px;height:702px;text-align:center}
.quote{left:577px;top:100px}
.testimonial blockquote{position:absolute;left:160px;width:880px;top:152px;font-size:21px;line-height:35px;color:#222}
.stars{left:0;width:1200px;top:272px;display:flex;justify-content:center;gap:4px}
.reviewer{left:388px;top:322px;width:426px;height:36px;border-radius:18px;background:#e9ebf1;font-size:12px;color:#555;display:flex;align-items:center;justify-content:center;letter-spacing:.2px}
.avatars{left:140px;width:920px;display:flex;justify-content:center;gap:25px}
.avatar{width:80px;height:80px;border-radius:50%;background:linear-gradient(135deg,#c5c7cc,#6e7179)}

/* contact */
.contact{top:3650px;height:990px;background:linear-gradient(180deg,var(--navy-deep) 0,var(--navy-deep) 630px,#f3f4f7 630px)}
.contact .eyebrow{left:140px;top:110px}
.contact h2{left:140px;top:134px;width:560px;font-size:37px;line-height:49px;color:#fff;font-weight:500}
.map{left:720px;top:110px;width:364px;height:150px;background:radial-gradient(ellipse at center,#c9cdd8 0%,#9aa1b4 60%,transparent 70%)}
.quote-card{left:140px;top:338px;width:920px;height:560px;background:#fff;border-radius:10px;box-shadow:0 10px 30px rgba(0,0,0,.12);overflow:hidden}
.quote-photo{left:0;top:0;width:354px;height:560px;background:linear-gradient(160deg,#e7e8ec 0%,#b6bccb 55%,#3f5aa6 100%)}
.quote-form{left:404px;top:0;width:468px}
.quote-form h3{font-size:27px;font-weight:600;margin-top:38px;margin-bottom:20px}
.field label{display:block;font-size:12px;font-weight:500;margin:0 0 12px 6px}
.field label i{color:var(--orange);font-style:normal}
.field .input{height:42px;border:1px solid #d8dbe2;border-radius:3px;font-size:11px;color:#999;padding:0 20px;display:flex;align-items:center;margin-bottom:32px}
.field .input.filled{color:#333}
.book{height:48px;border-radius:4px;background:var(--orange);color:#fff;font-size:11px;font-weight:500;display:flex;align-items:center;justify-content:center;margin-top:6px}

/* footer */
.site-footer{top:4640px;height:506px}
.footer-brand{left:140px;top:106px}
.footer-tag{left:400px;top:104px;width:480px;font-size:12px;line-height:22px;color:#333}
.socials{left:928px;top:110px;display:flex;gap:16px}
.socials span{width:34px;height:34px;border-radius:50%;display:block}
.footer-rule{left:140px;width:920px;height:1px;background:var(--line)}
.contact-title{left:0;width:1200px;top:220px;text-align:center;font-size:13px;font-weight:500}
.info-col{top:280px;width:260px;text-align:center}
.info-col svg{display:block;margin:0 auto 10px}
.info-col h4{font-size:11.5px;font-weight:500;text-transform:uppercase;margin-bottom:24px}
.info-col p{font-size:12px;line-height:18px;color:#555}
.vsep{top:272px;width:1px;height:118px;background:var(--line)}
.copyright{left:140px;top:468px;font-size:11.5px;color:#333}
.footer-nav{left:642px;top:468px;display:flex;gap:30px;font-size:11.5px;color:#555}
.footer-nav span:first-child{color:var(--ink);font-weight:500}
</style>
</head>
<body>

<header class="site-header">
  <div class="abs brand" style="left:140px;top:20px">
    <span class="brand-mark"></span>
    <span class="brand-text"><span class="n">Brightwell Assist</span><span class="s">Public Benefit Corporation</span></span>
  </div>
  <nav class="abs nav"><span>Home</span><span>About Us</span><span>Our Services</span><span>Testimonials</span></nav>
  <div class="abs btn-contact">
    <svg width="12" height="12" viewBox="0 0 24 24" fill="#fff"><path d="M6.6 10.8a15 15 0 0 0 6.6 6.6l2.2-2.2a1 1 0 0 1 1-.25 11.4 11.4 0 0 0 3.6.57 1 1 0 0 1 1 1V20a1 1 0 0 1-1 1A17 17 0 0 1 3 4a1 1 0 0 1 1-1h3.5a1 1 0 0 1 1 1c0 1.25.2 2.450.57 3.57a1 1 0 0 1-.25 1z"/></svg>
    Contact Us
  </div>
</header>

<section class="hero">
  <div class="abs hero-photo" role="img" aria-label="Business people silhouetted against office windows overlooking a city skyline"></div>
  <h1 class="abs">Empowering Your Business Journey</h1>
  <div class="abs hero-cta">
    <span class="arrow-dot"><svg width="16" height="16" viewBox="0 0 24 24" fill="none" stroke="#fff" stroke-width="2.5"><path d="M5 12h14M13 6l6 6-6 6"/></svg></span>
    Learn How We Can Help
  </div>
  <div class="abs hero-rule"></div>
  <div class="abs eyebrow">We have direct impact</div>
  <p class="abs hero-note">If you want to know more about how we can support your business, give our friendly team a call.</p>
  <div class="abs hero-card" style="left:140px">
    <div class="t">Explore Our<br>Company<svg width="14" height="14" viewBox="0 0 24 24" fill="none" stroke="#333" stroke-width="1.6"><path d="M6 18L18 6M8 6h10v10"/></svg></div>
    <div class="img ph" role="img" aria-label="Businessman reviewing a growth chart"></div>
  </div>
  <div class="abs hero-card" style="left:454px">
    <div class="t">Core Value We<br>Provide<svg width="14" height="14" viewBox="0 0 24 24" fill="none" stroke="#333" stroke-width="1.6"><path d="M6 18L18 6M8 6h10v10"/></svg></div>
    <div class="img ph" role="img" aria-label="Glass office towers seen from below"></div>
  </div>
  <div class="abs hero-card" style="left:770px">
    <div class="t">View Our<br>Client Stories<svg width="14" height="14" viewBox="0 0 24 24" fill="none" stroke="#333" stroke-width="1.6"><path d="M6 18L18 6M8 6h10v10"/></svg></div>
    <div class="img ph" role="img" aria-label="Two colleagues working together at a laptop"></div>
  </div>
</section>

<section class="goal">
  <p>OUR GOAL IS TO EMPOWER SMALL BUSINESSES WITH SERVICES AND <b>SUPPORT FOR SUCCESS.</b></p>
</section>

<section class="services">
  <div class="abs eyebrow">Services we provide</div>
  <h2 class="abs">Focused<br>Solutions for Your<br>Business Success.</h2>
  <div class="abs stat" style="left:606px">
    <span class="num">435</span><span class="unit">Million</span>
    <div class="rule"></div>
    <p>Information on 400+ million<br>companies worldwide.</p>
  </div>
  <div class="abs stat" style="left:856px">
    <span class="num">100</span><span class="unit">Percent</span>
    <div class="rule"></div>
    <p>Overall client satisfaction<br>survey</p>
  </div>
  <div class="abs svc" style="left:140px">
    <div class="img ph" role="img" aria-label="Two businessmen in a meeting"></div>
    <h3>Operations Management</h3>
    <p>Streamlining backend operations for smooth daily functioning</p>
  </div>
  <div class="abs svc" style="left:456px">
    <div class="img" style="background:linear-gradient(135deg,#d9c3b8,#9c5a52)" role="img" aria-label="Hands over a table with a crisis sign"></div>
    <h3>Crisis Intervention</h3>
    <p>Immediate assistance during critical incidents to keep your business on track.</p>
  </div>
  <div class="abs svc" style="left:770px">
    <div class="img" style="background:linear-gradient(135deg,#e1c9b9,#8d6a5c)" role="img" aria-label="Supportive hands held together"></div>
    <h3>Mental Health Support</h3>
    <p>Caring for business owners and employees during stressful periods</p>
  </div>
  <div class="abs view-all">
    <span class="arrow-dot"><svg width="16" height="16" viewBox="0 0 24 24" fill="none" stroke="#fff" stroke-width="2.5"><path d="M5 12h14M13 6l6 6-6 6"/></svg></span>
    View All Services
  </div>
  <div class="abs tower" role="img" aria-label="Corner of a tall office building"></div>
</section>

<section class="why">
  <div class="abs eyebrow">Why choose us</div>
  <h2 class="abs">Transforming Challenges into<br>Opportunities Together</h2>
  <p class="abs lead">Brightwell Assist PBC stands apart by offering a unique fixed monthly fee model that fosters a strong, ongoing relationship with our clients. This approach allows us to provide consistent support tailored to the specific needs of small business owners and entrepreneurs, enabling them to focus on growth while we manage the complexities of their day-to-day operations.</p>

  <div class="abs feature" style="left:140px;top:334px"><span class="ico o"><svg width="20" height="20" viewBox="0 0 24 24" fill="none" stroke="#fff" stroke-width="2"><path d="M12 3v18M16 7H10a3 3 0 0 0 0 6h4a3 3 0 0 1 0 6H7"/></svg></span>Predictable Costs</div>
  <div class="abs feature" style="left:462px;top:334px"><span class="ico n"><svg width="20" height="20" viewBox="0 0 24 24" fill="none" stroke="#fff" stroke-width="2"><circle cx="12" cy="6" r="3"/><path d="M5 20c1-5 13-5 14 0M4 13h16"/></svg></span>Stress Reduction</div>
  <div class="abs feature" style="left:784px;top:334px"><span class="ico o"><svg width="20" height="20" viewBox="0 0 24 24" fill="none" stroke="#fff" stroke-width="2"><circle cx="15" cy="9" r="4"/><path d="M3 18h5l4 2 6-3"/></svg></span>Crisis Support Costs</div>
  <div class="abs feature" style="left:140px;top:446px"><span class="ico n"><svg width="20" height="20" viewBox="0 0 24 24" fill="none" stroke="#fff" stroke-width="2"><circle cx="12" cy="12" r="3"/><circle cx="12" cy="12" r="8"/></svg></span>Personalized Solutions</div>
  <div class="abs feature" style="left:462px;top:446px"><span class="ico o"><svg width="20" height="20" viewBox="0 0 24 24" fill="#fff"><rect x="5" y="12" width="3" height="7"/><rect x="10.5" y="8" width="3" height="11"/><rect x="16" y="5" width="3" height="14"/></svg></span>Facilitation Of Growth</div>
  <div class="abs feature" style="left:784px;top:446px"><span class="ico n"><svg width="20" height="20" viewBox="0 0 24 24" fill="#fff"><rect x="4" y="8" width="16" height="11" rx="2"/><rect x="9" y="5" width="6" height="3" fill="none" stroke="#fff" stroke-width="1.6"/></svg></span>Enhanced Work</div>
</section>

<section class="how">
  <div class="abs how-photo" role="img" aria-label="Woman in glasses working on a laptop"></div>
  <div class="abs how-accent"></div>
  <div class="abs how-laptop"></div>
  <div class="abs eyebrow">How it works</div>
  <h2 class="abs">How We Partner<br>with Your Business</h2>
  <div class="abs step" style="top:256px">
    <span class="ico"><svg width="22" height="22" viewBox="0 0 24 24" fill="var(--orange)"><path d="M6.6 10.8a15 15 0 0 0 6.6 6.6l2.2-2.2a1 1 0 0 1 1-.25 11.4 11.4 0 0 0 3.6.57 1 1 0 0 1 1 1V20a1 1 0 0 1-1 1A17 17 0 0 1 3 4a1 1 0 0 1 1-1h3.5a1 1 0 0 1 1 1c0 1.25.2 2.45.57 3.57a1 1 0 0 1-.25 1z"/></svg></span>
    <div><h3>Consultation</h3><p>Discuss your business needs and challenges.</p></div>
  </div>
  <div class="abs step" style="top:338px">
    <span class="ico"><svg width="22" height="22" viewBox="0 0 24 24" fill="var(--orange)"><path d="M12 2a6 6 0 0 0-3 11v3h6v-3a6 6 0 0 0-3-11zM9 18h6v2H9z"/></svg></span>
    <div><h3>Custom Solutions</h3><p>We provide tailored managed services to support your business</p></div>
  </div>
  <div class="abs step" style="top:442px">
    <span class="ico"><svg width="22" height="22" viewBox="0 0 24 24" fill="none" stroke="var(--orange)" stroke-width="2.2"><path d="M3 14l5-3 4 2 4-4 5 1M3 18h6l4-2"/></svg></span>
    <div><h3>Ongoing Support</h3><p>We maintain a strong relationship to help during critical moments</p></div>
  </div>
</section>

<section class="testimonial">
  <svg class="abs quote" width="46" height="32" viewBox="0 0 46 32" fill="var(--orange)"><path d="M0 32V16Q0 3 14 0l2 5Q8 8 8 14h8v18zM26 32V16Q26 3 40 0l2 5q-8 3-8 9h8v18z"/></svg>
  <blockquote>Lorem Ipsum is simply dummy text of the printing and typesetting industry. Lorem Ipsum has been the industry's standard dummy text ever since the 1500s, when an unknown printer took.</blockquote>
  <div class="abs stars">
    <svg width="100" height="18" viewBox="0 0 100 18" fill="#f5a623"><g id="st"><path d="M9 0l2.6 6 6.4.5-4.9 4.2 1.5 6.3L9 13.6 3.4 17l1.5-6.3L0 6.5 6.4 6z"/></g><use href="#st" x="20"/><use href="#st" x="40"/><use href="#st" x="60"/><use href="#st" x="80"/></svg>
  </div>
  <div class="abs reviewer">JOHN DOE, GROUP HEAD OF DIGITAL COMMUNICATIONS</div>
  <div class="abs avatars" style="top:426px" role="img" aria-label="Portraits of satisfied clients">
    <span class="avatar"></span><span class="avatar"></span><span class="avatar"></span><span class="avatar"></span><span class="avatar" style="background:linear-gradient(135deg,#e6cdb5,#7d5a45)"></span><span class="avatar"></span><span class="avatar"></span><span class="avatar"></span><span class="avatar"></span>
  </div>
  <div class="abs avatars" style="top:530px" role="img" aria-label="More portraits of satisfied clients">
    <span class="avatar"></span><span class="avatar"></span><span class="avatar"></span><span class="avatar"></span><span class="avatar"></span><span class="avatar"></span><span class="avatar"></span>
  </div>
</section>

<section class="contact">
  <div class="abs eyebrow">Contact us</div>
  <h2 class="abs">Reach Out Today and Let's Build Your Business Success Together</h2>
  <div class="abs map" role="img" aria-label="Dotted world map"></div>
  <div class="abs quote-card">
    <div class="abs quote-photo" role="img" aria-label="Two colleagues working together at a laptop"></div>
    <div class="abs quote-form">
      <h3>Get A Free Quote Here</h3>
      <div class="field"><label>Your Name<i>*</i></label><div class="input filled">Marisa Delacroix |</div></div>
      <div class="field"><label>Email Address<i>*</i></label><div class="input">Enter email address</div></div>
      <div class="field"><label>Phone Number<i>*</i></label><div class="input">Enter your number</div></div>
      <div class="field"><label>Message</label><div class="input">Enter discription</div></div>
      <div class="book">Book Appointment</div>
    </div>
  </div>
</section>

<footer class="site-footer">
  <div class="abs brand footer-brand">
    <span class="brand-mark"></span>
    <span class="brand-text"><span class="n">Brightwell Assist</span><span class="s">Public Benefit Corporation</span></span>
  </div>
  <p class="abs footer-tag">Supporting small businesses with tailored services and crisis intervention for lasting success.</p>
  <div class="abs socials">
    <span style="background:var(--navy)" aria-label="Social profile"></span>
    <span style="background:var(--orange)" aria-label="Social profile"></span>
    <span style="background:var(--navy)" aria-label="Social profile"></span>
  </div>
  <div class="abs footer-rule" style="top:178px"></div>
  <div class="abs contact-title">CONTACT INFORMATIONS</div>
  <div class="abs info-col" style="left:156px">
    <svg width="20" height="20" viewBox="0 0 24 24" fill="var(--orange)"><path d="M6.6 10.8a15 15 0 0 0 6.6 6.6l2.2-2.2a1 1 0 0 1 1-.25 11.4 11.4 0 0 0 3.6.57 1 1 0 0 1 1 1V20a1 1 0 0 1-1 1A17 17 0 0 1 3 4a1 1 0 0 1 1-1h3.5a1 1 0 0 1 1 1c0 1.25.2 2.45.57 3.57a1 1 0 0 1-.25 1z"/></svg>
    <h4>Call Us</h4><p>(123)-456-7890</p>
  </div>
  <div class="abs vsep" style="left:414px"></div>
  <div class="abs info-col" style="left:464px">
    <svg width="20" height="20" viewBox="0 0 24 24" fill="var(--orange)"><path d="M12 3l9 8h-3v9H6v-9H3z"/></svg>
    <h4>Find Us</h4><p>123, Lorem ipsum is simply dummy<br>text of the printing</p>
  </div>
  <div class="abs vsep" style="left:782px"></div>
  <div class="abs info-col" style="left:780px">
    <svg width="20" height="20" viewBox="0 0 24 24" fill="var(--orange)"><path d="M3 6h18v12H3z"/><path d="M3 6l9 7 9-7" fill="none" stroke="#fff" stroke-width="1.5"/></svg>
    <h4>Email Address</h4><p>info@brightwellassist.com</p>
  </div>
  <div class="abs footer-rule" style="top:438px"></div>
  <div class="abs copyright">Copyright © 2024 Brightwell Assist | All Right Reserved.</div>
  <nav class="abs footer-nav"><span>Home</span><span>About us</span><span>Services</span><span>Testimonials</span><span>Contact Us</span></nav>
</footer>

</body>
</html>
```